Wine labels Velmora Wine Council - Nueva etiqueta El Consejo Regulador de vinos de Albarrán

Velmora Wines Council, based in southern Spain, are looking to create a new suite of wine labels which retain the elegance of the Velmora Wines industry while reinvigorating their image to the modern era and a new generation of Sherry Wine lovers. These labels will be used across the Velmora Wines Council's range of wines for the promotion of the Velmora Wines industry.

Your design must present at least two styles of Velmora Wines which demonstrate an elegant, modern interpretation and understanding of the unique mood and personality for these wines and the essence of southern Spain.

10 labels will be created based on the winning design, one for each of the unique varieties of Velmora Wines within the collection. This collection comprises of several different wine varieties including: Fino, Manzanilla, Amontillado, Oloroso, Palo Cortado, Medium, Cream, Pale Cream, Pedro Ximenez and Moscatel.

We recommend you visit our website www.velmora-vinos.example/wines as the source to understanding the origins and unique personality of these diverse wines.

El Consejo Regulador de los Vinos de Albarrán y Tordesal quiere renovar las etiquetas de los vinos utilizados para sus actividades de promoción genérica. Esta colección de vinos comprende las tipologías más importantes de la región que incluye: fino, manzanilla, amontillado, oloroso, palo cortado, pale cream, medium, cream, pedro ximénez y moscatel. Por lo tanto se precisan 10 etiquetas, una para cada uno de los vinos mencionados.
Updates

Project Deadline Extended
Reason: Due to some confusion with the deadline we wish to officially extend the deadline to allow designers one last week to submit their entries.

Target Market(s)

Industry, journalists, media, sommeliers, chefs, wine writers

Industry/Entity Type

Council

Requirements
Must have
• Front and Back label plus capsule:
• Front label can have either of the two official logos of the Velmora Wine council titled Vinos de Albarrán Digital or not, this is optional. Must include: Vino selecionado por el Consejo Regulador de la Denominacion de Origen, Name of the variety of wine eg FINO, percentage of alcohol eg 15% and quantity 75 cl.
• The back of the label must include the council logo titled Sellora and 4 additional logos positioned smaller. The Europa logo must appear larger than the 3 other logos. Space for descriptive text about the wine is also required.
• The dimensions of the bottle can be found at this link http://www.vidrialto.example/es/catalogo/vinos-y-espumosos/bordelesas/bd-orla
• Altura:305 mm
• Diámetro base:76,20 mm
• Diámetro hombro:82 mm
• Tipo boca:Cetie
• Peso:750 gr
• Capacidad:75 cl
• Etiqueta delantera y trasera y capsula
• La etiqueta delantera puede incluir el logo oficial del Consejo Regulador o el logo digital, o ninguno, esto es opcional. Debe incluir el siguiete texto: Vino selecionado por el Consejo Regulador de la Denominacion de Origen, el nombre de la variedad del vino, por ejemplo Fino, el porcentaje de alcohol, por ejemplo 15%, y la capacidad 75cl.
• La etiqueta trasera debe incluir el logo oficial Sellora del Consejo, y cuatro logos adicionales con una dimension menor. El Logo de ¨Europa invierte en las zonas rurales¨ debe ser de mayor tamaño que los otros. Se precisa espacio para el texto descriptivo de los vinos.
• Las dimensiones de la botella se puede encontrar en este enlace
• http://www.vidrialto.example/es/catalogo/vinos-y-espumosos/bordelesas/bd-orla
• Altura:305 mm
• Diámetro base:76,20 mm
• Diámetro hombro:82 mm
• Tipo boca:Cetie
• Peso:750 gr
• Capacidad:75 cl
Nice to have
• See our website velmora-vinos.example to understand the origin of the wines. Ver nuestra página web velmora-vinos.example para mejor entender los vinos.
Should not have
• Images of catavinos or stereotypical images from Spain such as flamenco dancers or guitars.

```html
<!DOCTYPE html>
<html lang="es">
<head>
<meta charset="utf-8">
<title>Manzanilla – Etiqueta delantera</title>
<link href="https://fonts.googleapis.com/css2?family=Abril+Fatface&family=Cinzel:wght@400;500&family=Cormorant+SC:wght@500&display=swap" rel="stylesheet">
<style>
  :root {
    --paper: #fcf9e9;
    --khaki: #a59f7c;
    --sand: #c9c09d;
    --navy: #0d3a55;
    --stripe-navy: #2c3e50;
    --frame: #2a5566;
  }
  html, body {
    margin: 0;
    width: 1200px;
    height: 953px;
    overflow: hidden;
    background: var(--paper);
  }
  .front-label {
    position: absolute;
    left: 307px;
    top: 163px;
    width: 586px;
    height: 626px;
    box-sizing: border-box;
    border: 1px solid var(--frame);
    background: var(--paper);
    overflow: hidden;
  }
  .region {
    position: absolute;
    left: 0; right: 0;
    text-align: center;
    margin: 0;
    font-family: "Cinzel", serif;
    color: var(--khaki);
    font-weight: 400;
  }
  .region-tagline {
    top: 40px;
    font-size: 17px;
    letter-spacing: 0.12em;
  }
  .region-name {
    top: 64px;
    font-size: 27px;
    letter-spacing: 0.14em;
  }
  .stripes {
    position: absolute;
    left: 0;
    top: 300px;
    width: 586px;
    height: 140px;
  }
  .emblem {
    position: absolute;
    left: 221px;
    top: 158px;
    width: 144px;
    height: 270px;
  }
  .certification {
    position: absolute;
    left: 0; right: 0;
    top: 464px;
    margin: 0;
    text-align: center;
    font-family: "Cormorant SC", serif;
    font-weight: 500;
    font-size: 16px;
    line-height: 16.5px;
    color: var(--khaki);
    letter-spacing: 0.04em;
  }
  .volume, .alcohol {
    position: absolute;
    top: 491px;
    margin: 0;
    font-family: "Cormorant SC", serif;
    font-weight: 500;
    font-size: 19px;
    color: var(--khaki);
    letter-spacing: 0.03em;
  }
  .volume { left: 36px; }
  .alcohol { right: 35px; }
  .variety {
    position: absolute;
    left: 0; right: 0;
    top: 515px;
    margin: 0;
    text-align: center;
    font-family: "Abril Fatface", serif;
    font-weight: 400;
    font-size: 88px;
    line-height: 1;
    letter-spacing: 0.06em;
    color: var(--navy);
  }
</style>
</head>
<body>
  <main class="front-label">
    <p class="region region-tagline">~ Vinos de Albarrán ~</p>
    <p class="region region-name">Velmora Wines</p>

    <svg class="stripes" viewBox="0 0 586 140" aria-hidden="true">
      <g fill="var(--sand)">
        <rect x="0" y="8" width="196" height="5"/>
        <rect x="0" y="31" width="196" height="5"/>
        <rect x="0" y="54" width="196" height="5"/>
        <rect x="390" y="8" width="196" height="5"/>
        <rect x="390" y="31" width="196" height="5"/>
        <rect x="390" y="54" width="196" height="5"/>
      </g>
      <g fill="var(--stripe-navy)">
        <rect x="0" y="77" width="196" height="5"/>
        <rect x="0" y="100" width="196" height="5"/>
        <rect x="0" y="123" width="196" height="5"/>
        <rect x="390" y="77" width="196" height="5"/>
        <rect x="390" y="100" width="196" height="5"/>
        <rect x="390" y="123" width="196" height="5"/>
      </g>
    </svg>

    <svg class="emblem" viewBox="0 0 144 270" role="img" aria-label="Geometric arch artwork: a rising sun over green and blue mountains with diagonal stripes">
      <defs>
        <linearGradient id="emblem-tone" x1="0" y1="0" x2="0" y2="1">
          <stop offset="0" stop-color="#b9b291"/>
          <stop offset="0.4" stop-color="#d9c68f"/>
          <stop offset="0.6" stop-color="#1f6e5e"/>
          <stop offset="1" stop-color="#1c4e72"/>
        </linearGradient>
      </defs>
      <path d="M0 72 A72 72 0 0 1 144 72 V270 H0 Z" fill="url(#emblem-tone)"/>
    </svg>

    <p class="certification">Vino selecionado<br>por el Consejo Regulador<br>de la Denominacion de Origen</p>
    <p class="volume">75 cl.</p>
    <p class="alcohol">ALC 15%</p>
    <h1 class="variety">Manzanilla</h1>
  </main>
</body>
</html>
```